Re-design a website for a millionaire mentor

We need an expert website designer to re-design the website vKeenstride.net

The website would have 4 pages. A home page, Summit Circle page, Hire RM page and an About page.

Here are some reference websites

https://www.lumovance.net
https://rolfbanter.net/

I will also attach a beginning of mockup of the home page I did myself to give an idea of the style we like, please use the quote "If you are not chasing your potential you are wasting your life" instead of the one in the current website...

You don't have the use the mockup (just the quote) and are free to use all your creativity.

Target Market(s)

Entrepreneurs

Number of Pages Required

4 page

Font styles to use
Other font styles liked:
• Franklin Gothic

Requirements
Must have
• -Call of action on the main page to download a free business plan
• -Hire rm page check out reference: http://www.hiremarkbellow.net
• -summit circle page with a button to sign in or join the summit circle. Check out reference for example: https://www.lumovance.net/glide_academy

```html
<!DOCTYPE html>
<html lang="en">
<head>
<meta charset="utf-8">
<title>vKeenstride — Home</title>
<link href="https://fonts.googleapis.com/css2?family=Saira:ital,wght@0,400;0,500;0,600;0,700;0,800;1,700&display=swap" rel="stylesheet">
<style>
:root{
  --red:#e3262b;
  --ink:#0b0b0b;
  --navy:#0b1538;
  --blue:#1a3fc4;
  --teal:#1a8fb0;
  --grey:#8e8f8f;
  --text:#555;
  --footer:#191919;
  --white:#fff;
}
*{margin:0;padding:0;box-sizing:border-box}
html,body{width:864px;height:1200px;overflow:hidden;background:var(--white)}
body{font-family:"Saira",sans-serif;position:relative}
.hero{position:absolute;left:0;top:0;width:864px;height:480px;
  clip-path:polygon(0 0,864px 0,864px 378px,0 480px);
  background:
   radial-gradient(ellipse 260px 300px at 640px 260px,#2a2a30 0%,rgba(20,20,30,.9) 45%,rgba(0,0,0,0) 75%),
   linear-gradient(172deg,#0d3fa8 0%,#1d78b8 10%,#0a2a8a 20%,var(--navy) 38%,#0a1030 70%,#081028 100%);}
.logo{position:absolute;left:82px;top:20px;display:flex;align-items:center;gap:8px;color:var(--white);
  font-weight:700;font-size:26px;letter-spacing:1px;line-height:1}
.logo .mark{width:20px;height:20px;background:var(--red)}
.nav{position:absolute;top:42px;left:418px;font-size:12px;font-weight:500;color:var(--white)}
.nav a{color:inherit;text-decoration:none;position:absolute;white-space:nowrap}
.headline{position:absolute;left:80px;top:150px;color:var(--white);font-weight:700;font-size:26px;line-height:44px}
.headline em{color:var(--red);font-style:italic;font-size:30px;margin:0 6px}
.sub{position:absolute;left:81px;top:242px;color:var(--white);font-weight:700;font-size:18px}
.btn{position:absolute;background:var(--red);color:var(--white);font-weight:700;display:flex;align-items:center;justify-content:center;text-decoration:none}
.btn-hero{left:82px;top:286px;width:119px;height:38px;font-size:13px;gap:8px}
.dots{position:absolute;top:378px;left:410px;display:flex;gap:8px;align-items:center}
.dots span{width:7px;height:7px;border-radius:50%;background:var(--white)}
.dots span.on{width:13px;height:13px;border:2px solid var(--white);background:transparent;position:relative}
.dots span.on::after{content:"";position:absolute;left:2px;top:2px;width:5px;height:5px;border-radius:50%;background:var(--white)}
.frame{position:absolute;left:56px;top:541px;width:252px;height:285px;border:4px solid var(--red)}
.shadow{position:absolute;left:93px;top:578px;width:252px;height:286px;background:var(--grey)}
.portrait{position:absolute;left:81px;top:566px;width:252px;height:286px;
  background:linear-gradient(135deg,#6b5c4a 0%,#c7b96a 30%,#3a8bb0 55%,#b44a7c 75%,#1b1b1b 100%)}
.about h2{position:absolute;left:413px;top:564px;font-size:35px;font-weight:800;color:var(--ink)}
.about p{position:absolute;left:417px;top:624px;width:367px;font-size:11px;line-height:20.5px;color:var(--text);text-align:justify;letter-spacing:0}
.btn-read{left:417px;top:785px;width:116px;height:35px;font-size:13px}
.footer{position:absolute;left:0;top:878px;width:864px;height:322px;background:var(--footer);
  clip-path:polygon(0 82px,864px 0,864px 322px,0 322px);color:var(--white)}
.col{position:absolute;top:104px}
.col h3{font-size:18px;font-weight:500;letter-spacing:.5px}
.col ul{list-style:none;margin-top:14px}
.col li{font-size:10.5px;font-weight:500;height:21px;display:flex;align-items:center;gap:7px}
.col li svg{width:6px;height:9px}
.contact dl{margin-top:12px;font-size:9.5px;line-height:15px}
.contact .row{display:flex;gap:5px;margin-bottom:8px}
.contact dt{font-weight:600;font-size:10px}
.contact dd{color:#ddd}
.social{display:flex;gap:7px;margin-top:14px;margin-left:6px}
.social span{width:19px;height:19px;border:1.3px solid var(--white);border-radius:50%}
.copy{position:absolute;left:0;width:864px;top:282px;text-align:center;font-size:9.5px;font-weight:500}
</style>
</head>
<body>
<header class="hero" role="img" aria-label="Stage photo of the mentor speaking into a microphone under blue lights"></header>
<div class="logo"><span class="mark"></span>KEEN STRIDE</div>
<nav class="nav">
  <a style="left:0">Home</a>
  <a style="left:59px">Summit Circle</a>
  <a style="left:157px">Hire RM</a>
  <a style="left:225px">About Us</a>
  <a style="left:302px">Contact Us</a>
</nav>
<h1 class="headline">If You Are Not Chasing Your <em>Potential</em><br>You Are <em>Wasting</em> Your Life</h1>
<p class="sub">Download My Free Business Plan</p>
<a class="btn btn-hero" href="#"><svg width="18" height="16" viewBox="0 0 18 16" fill="none" stroke="#fff" stroke-width="1.4"><path d="M1 8h10M8 4l4 4-4 4M7 1h9v14H7"/></svg>Click Here</a>
<div class="dots"><span class="on"></span><span></span><span></span></div>

<section class="about">
  <div class="frame"></div>
  <div class="shadow"></div>
  <div class="portrait" role="img" aria-label="Portrait of the mentor smiling in front of a graffiti wall"></div>
  <h2>About Us</h2>
  <p>Sed ut perspiciatis unde omnis iste natus error sit voluptatem accusantium doloremque laudantium, totam rem aperiam, eaque ipsa quae ab illo inventore veritatis et quasi architecto beatae vitae dicta sunt explicabo. Nemo enim ipsam voluptatem quia voluptas sit aspernatur aut odit aut fugit, sed quia consequuntur magni dolores eos qui ratione voluptatem sequi nesciunt. Neque porro quisquam est, qui dolorem ipsum quia dolor sit amet, consectetur, adipisci velit</p>
  <a class="btn btn-read" href="#">Read More</a>
</section>

<footer class="footer">
  <div class="col" style="left:84px"><h3>Quick Links</h3>
    <ul>
      <li><svg viewBox="0 0 6 9"><path d="M1 1l3.5 3.5L1 8" stroke="#fff" fill="none" stroke-width="1.2"/></svg>Home</li>
      <li><svg viewBox="0 0 6 9"><path d="M1 1l3.5 3.5L1 8" stroke="#fff" fill="none" stroke-width="1.2"/></svg>Summit Circle</li>
      <li><svg viewBox="0 0 6 9"><path d="M1 1l3.5 3.5L1 8" stroke="#fff" fill="none" stroke-width="1.2"/></svg>Hire RM</li>
      <li><svg viewBox="0 0 6 9"><path d="M1 1l3.5 3.5L1 8" stroke="#fff" fill="none" stroke-width="1.2"/></svg>About Us</li>
      <li><svg viewBox="0 0 6 9"><path d="M1 1l3.5 3.5L1 8" stroke="#fff" fill="none" stroke-width="1.2"/></svg>Contact Us</li>
    </ul></div>
  <div class="col" style="left:246px"><h3>Support</h3>
    <ul>
      <li><svg viewBox="0 0 6 9"><path d="M1 1l3.5 3.5L1 8" stroke="#fff" fill="none" stroke-width="1.2"/></svg>Contact Us</li>
      <li><svg viewBox="0 0 6 9"><path d="M1 1l3.5 3.5L1 8" stroke="#fff" fill="none" stroke-width="1.2"/></svg>Privacy Policy</li>
      <li><svg viewBox="0 0 6 9"><path d="M1 1l3.5 3.5L1 8" stroke="#fff" fill="none" stroke-width="1.2"/></svg>Terms &amp; Conditions</li>
      <li><svg viewBox="0 0 6 9"><path d="M1 1l3.5 3.5L1 8" stroke="#fff" fill="none" stroke-width="1.2"/></svg>Careers</li>
      <li><svg viewBox="0 0 6 9"><path d="M1 1l3.5 3.5L1 8" stroke="#fff" fill="none" stroke-width="1.2"/></svg>Support</li>
    </ul></div>
  <div class="col contact" style="left:433px"><h3>Contact Us</h3>
    <dl>
      <div class="row" style="margin-left:5px"><dt>Address:</dt><dd>4720 Copperleaf Ln<br>Suite # 310, Marlow, OR, 97402</dd></div>
      <div class="row" style="margin-left:5px"><dt>Phone:</dt><dd>(541) 203 7784</dd></div>
      <div class="row" style="margin-left:5px"><dt>Fax:</dt><dd style="margin-left:14px">1-541-203-7785</dd></div>
      <div class="row" style="margin-left:5px"><dt>Email:</dt><dd>info@vkeenstride.net</dd></div>
    </dl></div>
  <div class="col" style="left:660px"><h3>Stay Connected</h3>
    <div class="social" aria-label="Social links"><span></span><span></span><span></span><span></span></div></div>
  <p class="copy">© 2019 Copyrights | All Rights Reserved</p>
</footer>
</body>
</html>
```